Popup Nightclub Grand Opening Flyer

We need to design a flyer for the grand opening of an upscale, exclusive nightclub called "Lanternfall". The design needs to be chic and exclusive. The background should be black and the text should primarily be white. We like minimalist designs.

Here is the text for the flyer
-
Velvetrope Atlanta Presents

Lanternfall (LOGO)

A Popup Nightclub Experience
For one night Only

Friday, October 18, 2013
Party begins at 9PM

INVITE ONLY

See invitation for location details
(Velvetrope Atlanta logo)

-
Examples we like

http://cdn2-b.brivelpost.com/sites/default/files/styles/image_content_width/hash/3d/fa/1472093815_4471_flyer.jpg?itok=R8kqWm2z

http://api.plovra.com/files/7Kqq-Tr82XXB3pQzJvmtR5HL2W719E4nbRtC6KLd4HsfM8Y2qTDK-VmjwDoNqLX4QBzTHD9nakRbVx3m-Pfq8htc3MDTWr5p4/2zelSaturdays.jpg

http://quenmar.com/wp-content/uploads/yootheme/widgetkit/gallery/2zel/2zel-gen_vroom4-01.jpg

Hi All, one thing that we are seeing that we don't like is on over emphasis on the phrase "a popup nightclub experience" please don't make this the largest thing on the flyer

Target Market(s)

Target market is 25-35 year olds who are affluent (rich) and like luxury brands

Requirements
Must have
• Dark Background
Nice to have
• Velvetrope Logo on the bottom
Modern text that isn't curvy
Should not have
• Curved text

```html
<!DOCTYPE html>
<html lang="en">
<head>
<meta charset="utf-8">
<title>Lanternfall Nightclub – Popup Flyer</title>
<link rel="stylesheet" href="https://fonts.googleapis.com/css2?family=Antonio:wght@500&family=Josefin+Sans:wght@300;400&family=Questrial&display=swap">
<style>
  :root {
    --stage: #8e8e8e;
    --flyer-black: #0b0b0b;
    --flyer-glow: #2a2a2a;
    --ink: #ffffff;
    --ink-soft: #e6e6e6;
    --mark-grey: #bdbdbd;
  }
  * { margin: 0; padding: 0; box-sizing: border-box; }
  html, body {
    width: 971px;
    height: 1200px;
    overflow: hidden;
    background: var(--stage);
  }
  .flyer {
    position: absolute;
    left: 152px;
    top: 107px;
    width: 668px;
    height: 979px;
    background: radial-gradient(ellipse 70% 45% at 50% 38%, var(--flyer-glow) 0%, var(--flyer-black) 75%);
    color: var(--ink);
    font-family: "Questrial", "Century Gothic", sans-serif;
    overflow: hidden;
  }
  .line {
    position: absolute;
    left: 0;
    width: 100%;
    text-align: center;
    line-height: 1;
    transform: translateY(-50%);
    white-space: nowrap;
  }
  .presenter { top: 34px; font-size: 12px; letter-spacing: 0.3px; color: var(--ink-soft); }
  .club-mark {
    position: absolute;
    left: 50%;
    top: 102px;
    width: 62px;
    height: 62px;
    margin-left: -31px;
    margin-top: -31px;
    border-radius: 50%;
    background: var(--mark-grey);
  }
  .club-name {
    top: 204px;
    font-family: "Josefin Sans", sans-serif;
    font-weight: 300;
    font-size: 34px;
    letter-spacing: 5px;
    padding-left: 5px;
  }
  .club-type {
    top: 240px;
    font-family: "Josefin Sans", sans-serif;
    font-weight: 300;
    font-size: 18px;
    letter-spacing: 3px;
    padding-left: 3px;
  }
  .tagline-intro { top: 473px; font-size: 27px; letter-spacing: 1.5px; }
  .tagline-main {
    top: 530px;
    font-family: "Antonio", sans-serif;
    font-weight: 500;
    font-size: 76px;
    letter-spacing: 0.5px;
  }
  .tagline-outro { top: 590px; font-size: 34px; letter-spacing: 1.5px; }
  .tagline-close { top: 639px; font-size: 48px; letter-spacing: 2px; }
  .event-date { top: 762px; font-size: 25px; }
  .event-time { top: 792px; font-size: 25px; }
  .entry-policy { top: 864px; font-size: 36px; }
  .location-note {
    position: absolute;
    left: 44px;
    top: 953px;
    transform: translateY(-50%);
    font-size: 19px;
    line-height: 1;
    white-space: nowrap;
  }
  .host-brand {
    position: absolute;
    left: 435px;
    top: 953px;
    transform: translateY(-50%);
    display: flex;
    align-items: center;
    gap: 8px;
    font-size: 19px;
    letter-spacing: 2px;
    line-height: 1;
  }
  .host-dot {
    width: 26px;
    height: 26px;
    border-radius: 50%;
    background: var(--mark-grey);
  }
</style>
</head>
<body>
  <main class="flyer">
    <p class="line presenter">VELVETROPE ATLANTA PRESENTS</p>

    <div class="club-mark" aria-hidden="true"></div>
    <h1 class="line club-name">LANTERNFALL</h1>
    <p class="line club-type">NIGHTCLUB</p>

    <p class="line tagline-intro">A POPUP NIGHTCLUB</p>
    <p class="line tagline-main">EXPERIENCE</p>
    <p class="line tagline-outro">FOR ONE NIGHT</p>
    <p class="line tagline-close">ONLY</p>

    <p class="line event-date">FRIDAY, OCTOBER 18, 2013</p>
    <p class="line event-time">PARTY BEGINS AT 9PM</p>

    <p class="line entry-policy">INVITE ONLY</p>

    <p class="location-note">SEE INVITATION FOR LOCATION DETAILS</p>
    <div class="host-brand">
      <span class="host-dot" aria-hidden="true"></span>
      <span class="host-name">VELVETROPE</span>
    </div>
  </main>
</body>
</html>
```